Can You Help Sell Glass Cabinets with a Banner Ad?

Our New Zealand-based company designs and sells glass cabinets and display cases. 75% of our customers are other businesses who want to display products in their shop or showroom. The other 25% of our customers are householders who want a glass cabinet for their personal collectables. We have been trading 2 years now, and are expanding rapidly. Our website address is www.vitrinaplace.example.nz.
We have made a strategic decision to focus on online advertising this year. This is because we want to raise our profile to the greatest number of and widest range of people. For now, this means banner advertising on high traffic New Zealand-based websites in an attempt to generate more traffic to our website. The websites we will initially use are www.ploverpost.example.nz and www.tuidaily.example.nz.
We therefore need a set of eye-catching banner ads designed for our online marketing campaign. The three banners required will probably just be variations on a single design.

Banner 1: Top Banner
760x120

Banner 2: Skyscraper
160x600

Banner 3: Medium Rectangle
300x250

Target Market(s)

The primary target market will be retailers who have shops and showrooms. They may not yet know they need a showcase.

Industry/Entity Type

Advertising

Requirements
Must have
• Vitrina Place logo
"High quality glass cabinets and showcases"
Maybe also "Show your products, not the cabinet"
[Corporate colour is green, as per logo. Secondary colours are orange, purple and grey.]
[Please use New Zealand (British) spelling]

Nice to have
• Please view our website and brochure on the Resources page for the look and feel of our company. In particular we like our logo, so it is possible you can take a lead from this. The logo emblem is designed to be evocative of glass.
The logo spot colour is 41,0,70,10.

```html
<!DOCTYPE html>
<html lang="en-NZ">
<head>
<meta charset="utf-8">
<title>Vitrina Place – Banner Set</title>
<link rel="stylesheet" href="https://fonts.googleapis.com/css2?family=Open+Sans:wght@600&family=PT+Sans+Narrow:wght@700&family=Vollkorn:wght@700&display=swap">
<style>
  :root {
    --backdrop: #3c4a50;
    --green: #8dc43f;
    --green-light: #a3d255;
    --green-deep: #78b02e;
    --logo-green: #8cc04a;
    --white: #ffffff;
    --orange-top: #fbbf3c;
    --orange-bottom: #f18a0c;
    --orange-edge: #c9700a;
    --photo-warm: #c9a583;
    --photo-cool: #d9dde0;
    --product-dark: #3a3d40;
    --product-grey: #b9bdc0;
  }
  * { box-sizing: border-box; margin: 0; padding: 0; }
  html, body { width: 1200px; height: 562px; overflow: hidden; }
  body { background: var(--backdrop); position: relative; font-family: "Open Sans", sans-serif; }

  .banner {
    position: absolute; left: 94px; width: 1003px; height: 172px; overflow: hidden;
    background: linear-gradient(135deg, var(--green-light) 0%, var(--green) 45%, var(--green-deep) 100%);
  }
  .banner--top { top: 77px; }
  .banner--split { top: 305px; }

  .brand { position: absolute; display: flex; align-items: center; gap: 10px; }
  .brand__mark { width: 40px; height: 40px; border-radius: 4px; }
  .brand__name { font-family: "Open Sans", sans-serif; font-weight: 600; font-size: 25px; letter-spacing: 0.2px; line-height: 1; white-space: nowrap; }

  .banner--top .brand { left: 25px; top: 20px; }
  .banner--top .brand__mark { background: rgba(255,255,255,0.45); }
  .banner--top .brand__name { color: var(--white); }

  .headline { position: absolute; font-family: "Vollkorn", serif; font-weight: 700; font-size: 32px; color: var(--white); line-height: 1; white-space: nowrap; }
  .subline { position: absolute; font-family: "PT Sans Narrow", sans-serif; font-weight: 700; font-size: 32px; color: var(--white); line-height: 1; white-space: nowrap; }

  .banner--top .headline { left: 23px; top: 79px; }
  .banner--top .subline { left: 23px; top: 117px; }

  .cta {
    position: absolute; display: flex; align-items: center; justify-content: center; gap: 8px;
    border: 1px solid var(--orange-edge); border-radius: 4px;
    background: linear-gradient(var(--orange-top), var(--orange-bottom));
    color: var(--white); font-family: "PT Sans Narrow", sans-serif; font-weight: 700; font-size: 19px;
    text-decoration: none; box-shadow: 0 1px 2px rgba(0,0,0,0.25); white-space: nowrap;
  }
  .cta svg { width: 18px; height: 14px; }
  .banner--top .cta { left: 450px; top: 118px; width: 190px; height: 35px; }

  .photo { position: absolute; border: 6px solid var(--white); box-shadow: 0 2px 6px rgba(0,0,0,0.35); }
  .photo--showroom { left: 679px; top: 14px; width: 145px; height: 140px; transform: rotate(-4deg);
    background: linear-gradient(160deg, var(--photo-cool) 0%, #c8c2bd 55%, #9b2a2e 100%); }
  .photo--stairway { left: 793px; top: 6px; width: 176px; height: 155px; transform: rotate(4deg);
    background: linear-gradient(150deg, #f2efe9 0%, var(--photo-warm) 55%, #a97a4f 100%); }

  .banner--split .panel { position: absolute; left: 0; top: 0; width: 360px; height: 172px; }
  .banner--split .brand { left: 26px; top: 46px; }
  .banner--split .brand__mark { background: rgba(140,192,74,0.35); }
  .banner--split .brand__name { color: var(--logo-green); }
  .banner--split .cta { left: 63px; top: 109px; width: 218px; height: 39px; font-size: 21px; }
  .banner--split .headline { left: 365px; top: 14px; }
  .banner--split .subline { left: 368px; top: 71px; font-size: 36px; }

  .product { position: absolute; opacity: 0.9; border-radius: 2px; }
  .product--case { left: 768px; top: 117px; width: 62px; height: 53px;
    background: linear-gradient(180deg, #4a4d50, var(--product-dark)); }
  .product--towers { left: 840px; top: 51px; width: 163px; height: 121px;
    background: linear-gradient(90deg, var(--product-dark) 0%, #6d7175 45%, var(--product-grey) 100%); }
</style>
</head>
<body>

<section class="banner banner--top" aria-label="Top banner">
  <div class="brand"><span class="brand__mark"></span><span class="brand__name">VITRINA PLACE</span></div>
  <h1 class="headline">High Quality Glass Cabinets &amp; Showcases</h1>
  <p class="subline">Show your products, not the cabinet</p>
  <a class="cta" href="#">View Our Products
    <svg viewBox="0 0 18 14"><path d="M2 2l5 5-5 5M9 2l5 5-5 5" fill="none" stroke="#fff" stroke-width="2.6"/></svg>
  </a>
  <div class="photo photo--showroom" role="img" aria-label="Photo of a glass counter showcase in a showroom"></div>
  <div class="photo photo--stairway" role="img" aria-label="Photo of a tall glass display cabinet beside a staircase"></div>
</section>

<section class="banner banner--split" aria-label="Split banner">
  <svg class="panel" viewBox="0 0 360 172" preserveAspectRatio="none" aria-hidden="true">
    <path d="M0 0H331C300 40 300 132 336 172H0Z" fill="#ffffff"/>
  </svg>
  <div class="brand"><span class="brand__mark"></span><span class="brand__name">VITRINA PLACE</span></div>
  <a class="cta" href="#">View Our Products
    <svg viewBox="0 0 18 14"><path d="M2 2l5 5-5 5M9 2l5 5-5 5" fill="none" stroke="#fff" stroke-width="2.6"/></svg>
  </a>
  <h2 class="headline">High Quality Glass Cabinets &amp; Showcases</h2>
  <p class="subline">Show your products, not the cabinet</p>
  <div class="product product--case" role="img" aria-label="Product shot of a portable display case"></div>
  <div class="product product--towers" role="img" aria-label="Product shots of tall glass tower cabinets"></div>
</section>

</body>
</html>
```